Can you make a cool and versatile Talvern Ridge Powerpoint template?
See www.talvernridge.co.uk and http://www.linkedin.com/company/talvern-ridge-ltd/ (on the right) to see how the logos are currently used - with interchangeably white and black backgrounds.
Target Market(s)
Marketing managers, product managers in HR technology, HR consultants
Industry/Entity Type
It Company
Font styles to use
Sans Serif
Requirements
Must have
- Master slide design, fonts, color theme, etc. Ideally two variations - one with white background (using colorful logo), one with a darker background (using black/white logo).

```html
<!DOCTYPE html>
<html lang="en">
<head>
<meta charset="utf-8">
<title>Introduction to Talvern Ridge – Business overview</title>
<link rel="stylesheet" href="https://fonts.googleapis.com/css2?family=Fira+Sans+Extra+Condensed:wght@300;600&family=Source+Sans+3:wght@400&display=swap">
<style>
  :root {
    --page: #ffffff;
    --band-top: #4e4e50;
    --band-bottom: #48484a;
    --band-glow: #5a5a5c;
    --stage: #000000;
    --feature-tone: #3a3a3c;
    --title-light: #8c8c8e;
    --ink-white: #ffffff;
  }
  html, body {
    margin: 0;
    padding: 0;
    width: 1200px;
    height: 1000px;
    overflow: hidden;
    background: var(--page);
  }
  .slide {
    position: absolute;
    left: 35px;
    top: 80px;
    width: 1130px;
    height: 835px;
    background: var(--stage);
    overflow: hidden;
  }
  .header-band {
    position: absolute;
    left: 0;
    top: 0;
    width: 100%;
    height: 357px;
    background:
      radial-gradient(ellipse 700px 420px at 85% 70%, var(--band-glow), transparent 70%),
      linear-gradient(180deg, var(--band-top), var(--band-bottom));
  }
  .brand-tab {
    position: absolute;
    left: 0;
    top: 36px;
    width: 238px;
    height: 77px;
    background: var(--stage);
    border-radius: 0 38px 38px 0;
    display: flex;
    align-items: center;
    gap: 10px;
    padding-left: 24px;
    box-sizing: border-box;
  }
  .brand-dot {
    width: 12px;
    height: 12px;
    border-radius: 50%;
    background: var(--ink-white);
    flex: none;
  }
  .brand-name {
    font-family: "Fira Sans Extra Condensed", sans-serif;
    font-weight: 600;
    font-size: 21px;
    letter-spacing: 0.5px;
    text-transform: uppercase;
    color: var(--ink-white);
  }
  .feature-art {
    position: absolute;
    left: 0;
    top: 357px;
    width: 700px;
    height: 478px;
    background: radial-gradient(ellipse 520px 420px at 38% 68%, var(--feature-tone), transparent 72%);
  }
  .title {
    position: absolute;
    right: 68px;
    top: 200px;
    margin: 0;
    text-align: right;
    font-family: "Fira Sans Extra Condensed", sans-serif;
    text-transform: uppercase;
    line-height: 1;
  }
  .title-lead {
    display: block;
    font-weight: 300;
    font-size: 66px;
    color: var(--title-light);
    letter-spacing: -1px;
  }
  .title-name {
    display: block;
    font-weight: 600;
    font-size: 76px;
    color: var(--ink-white);
    margin-top: -2px;
  }
  .subtitle {
    position: absolute;
    right: 83px;
    top: 455px;
    margin: 0;
    font-family: "Source Sans 3", sans-serif;
    font-weight: 400;
    font-size: 52px;
    color: var(--ink-white);
  }
  .date {
    position: absolute;
    right: 83px;
    top: 677px;
    margin: 0;
    font-family: "Source Sans 3", sans-serif;
    font-size: 22px;
    color: var(--ink-white);
    text-transform: uppercase;
  }
</style>
</head>
<body>
  <main class="slide">
    <header class="header-band">
      <div class="brand-tab">
        <span class="brand-dot"></span>
        <span class="brand-name">Talvern Ridge</span>
      </div>
    </header>

    <div class="feature-art" role="img" aria-label="Large white brand graphic in the lower left corner"></div>

    <h1 class="title">
      <span class="title-lead">Introduction to</span>
      <span class="title-name">Talvern Ridge</span>
    </h1>

    <p class="subtitle">Business overview</p>
    <p class="date">16 November 2013</p>
  </main>
</body>
</html>
```